I need professional letterhead for an attorney. I already have my logo (attached). I currently have a project going to get business cards. I would like the letterhead to be classy. It is very important that this letterhead be in a format that I can import it into Microsoft Word 2013. I plan on importing this into Word so I can type my documents directly onto it and electronically send the finished documents to my clients. Thank you very much.

Industry/Entity Type

Attorney

Requirements
Must have
• Here is my info. Please put it all on there:
• Dwight R. Mallory Attorney At Law
• 48613 Brackwell Crescent
• St. Louis, MO 63047
• Telephone: 314-596-2043
• Fax: 800-627-4915
• Email: Dwight@RivermarkWills.com
• Also, I need the ability to import this final design into Microsoft Word 2013 so that I can type directly onto it. I believe I can do that if you hand it over to me as a JPG and a PDF in addition to the other formats. Then I should be able to import it into Word.

```html
<!DOCTYPE html>
<html lang="en">
<head>
<meta charset="utf-8">
<title>Rivermark Wills LLC — Letterhead</title>
<link rel="stylesheet" href="https://fonts.googleapis.com/css2?family=Tinos:wght@400&display=swap">
<style>
  :root {
    --brand-blue: #2f8fd1;
    --brand-blue-pale: #e3eef7;
    --ink: #2b2b2b;
    --rule: #9aa0a6;
    --paper: #ffffff;
  }
  html, body {
    margin: 0;
    padding: 0;
    width: 849px;
    height: 1200px;
    overflow: hidden;
    background: var(--paper);
  }
  .letterhead {
    position: relative;
    width: 849px;
    height: 1200px;
    overflow: hidden;
    background: var(--paper);
    font-family: "Tinos", "Times New Roman", serif;
    color: var(--ink);
  }
  .firm-mark {
    position: absolute;
    left: 44px;
    top: 90px;
    display: flex;
    align-items: center;
    gap: 12px;
  }
  .firm-mark__dot {
    width: 46px;
    height: 46px;
    border-radius: 50%;
    background: var(--brand-blue);
    flex: none;
  }
  .firm-mark__name {
    font-size: 24px;
    font-weight: 400;
    color: var(--brand-blue);
    letter-spacing: 0.5px;
    white-space: nowrap;
  }
  .attorney-address,
  .contact-lines {
    position: absolute;
    top: 92px;
    font-size: 11.5px;
    line-height: 15px;
    font-style: normal;
    white-space: nowrap;
  }
  .attorney-address {
    right: 240px;
    text-align: right;
  }
  .contact-lines {
    left: 632px;
  }
  .contact-lines p,
  .attorney-address p { margin: 0; }
  .header-rule {
    position: absolute;
    left: 40px;
    right: 0;
    top: 150px;
    height: 0;
    border-top: 1px solid var(--rule);
  }
  .corner-accent {
    position: absolute;
    left: 722px;
    top: 900px;
  }
</style>
</head>
<body>
  <main class="letterhead">
    <header>
      <div class="firm-mark">
        <span class="firm-mark__dot"></span>
        <span class="firm-mark__name">RIVERMARK WILLS LLC</span>
      </div>
      <address class="attorney-address">
        <p>Dwight R. Mallory Attorney At Law</p>
        <p>48613 Brackwell Crescent</p>
        <p>St. Louis, MO 63047</p>
      </address>
      <div class="contact-lines">
        <p>Telephone: 314-596-2043</p>
        <p>Fax: 800-627-4915</p>
        <p>Email: Dwight@RivermarkWills.com</p>
      </div>
      <div class="header-rule"></div>
    </header>
    <svg class="corner-accent" width="127" height="300" viewBox="0 0 127 300" aria-hidden="true">
      <circle cx="140" cy="150" r="130" fill="var(--brand-blue-pale)"/>
    </svg>
  </main>
</body>
</html>
```